VFX Company Business Card Design Project

The Ember Vale is a decentralized Visual Effects Studio servicing the television and feature film industries.
Project Brief:
Take our logo that was previously designed on Pixel Harbor and make a double sided business card.
Requirements:
- Card MUST be double sided.
- Front of card MUST have the yellow part of our logo against the dark grey background.
- Back of card is completely up to the designer.
- Back of card must include the complete company logo.
Please follow these File Preparation guidelines:
http://printmoor.example/infopage?file=filetype_en&s=PrintMoor_new&lang=en
Industry/Entity Type
Business
Look and feel
Each slider illustrates characteristics of the customer's brand and the style your logo design should communicate.

```html
<!DOCTYPE html>
<html lang="en">
<head>
<meta charset="utf-8">
<title>The Ember Vale — Business Card</title>
<link rel="stylesheet" href="https://fonts.googleapis.com/css2?family=Open+Sans:wght@400;600;700&display=swap">
<style>
  :root {
    --backdrop: #8f8f91;
    --card-dark: #2a2a2a;
    --card-light: #f6f6f6;
    --accent: #f8c21c;
    --ink: #2e2e2e;
    --ink-soft: #444444;
    --on-dark: #e9e9e9;
  }
  * { box-sizing: border-box; margin: 0; padding: 0; }
  html, body {
    width: 1200px; height: 800px; overflow: hidden;
    background: var(--backdrop);
    font-family: "Open Sans", Arial, sans-serif;
  }
  .stage {
    width: 1200px; height: 800px;
    display: flex; align-items: center; justify-content: center; gap: 40px;
  }
  .card {
    width: 520px; height: 297px;
    box-shadow: 0 6px 18px rgba(0,0,0,0.25);
    position: relative; overflow: hidden;
  }
  /* Front */
  .card--front {
    background: var(--card-dark);
    display: flex; flex-direction: column; align-items: center; justify-content: center;
  }
  .brand {
    display: flex; align-items: center; gap: 12px;
    color: var(--accent); font-weight: 700; letter-spacing: 0.5px;
  }
  .brand__dot {
    width: 18px; height: 18px; border-radius: 50%; background: var(--accent);
  }
  .card--front .brand { font-size: 40px; }
  .card--front .web {
    margin-top: 18px; color: var(--on-dark);
    font-size: 17px; font-weight: 600;
  }
  /* Back */
  .card--back { background: var(--card-light); }
  .holder {
    position: absolute; top: 28px; left: 0; right: 0;
    text-align: center; padding-left: 60px; color: var(--ink);
  }
  .holder__name { font-size: 17px; font-weight: 700; line-height: 1.1; }
  .holder__title { font-size: 13px; line-height: 1.2; color: var(--ink-soft); }
  .band {
    position: absolute; top: 92px; left: 0; right: 0; height: 92px;
    background: var(--card-dark);
    display: flex; align-items: center; justify-content: center;
  }
  .band .brand { font-size: 34px; }
  .contact {
    position: absolute; top: 200px; left: 0; right: 0;
    text-align: center; color: var(--ink);
    font-size: 14px; line-height: 1.5;
  }
  .contact__label { color: var(--accent); font-weight: 700; margin-right: 3px; }
  .contact__sep { display: inline-block; width: 12px; }
</style>
</head>
<body>
  <main class="stage">
    <section class="card card--front" aria-label="Card front">
      <div class="brand"><span class="brand__dot"></span>The Ember Vale</div>
      <p class="web">embervale.example</p>
    </section>

    <section class="card card--back" aria-label="Card back">
      <div class="holder">
        <p class="holder__name">Mara Linden</p>
        <p class="holder__title">Managing Director</p>
      </div>
      <div class="band">
        <div class="brand"><span class="brand__dot"></span>The Ember Vale</div>
      </div>
      <div class="contact">
        <p>480 Harrow Lane Suite 12, Kelridge, BC V0X2Q4, CA</p>
        <p><span class="contact__label">T</span>(555) 014-2291<span class="contact__sep"></span><span class="contact__label">F</span>(555) 014-7730</p>
        <p><span class="contact__label">E</span>m.linden@embervale.example</p>
      </div>
    </section>
  </main>
</body>
</html>
```